New Custom Pizza Box Design Project For Independant Restaurant

We are looking for creative designs for our new custom printed pizza boxes. Designs should include the following:

-Our logo & company name
-A color scheme similar to our current logo
-Our physical and URL addresses & phone number (menu is attached)
-Ability to scale the design across several box sizes (10x10x2, 14x14x2, 18x13x2,
26x18x2)
- Any creative flair you think will make for the best design

Design can be on a white or kraft (tan) box.
Designs can be either two or three ink colors.

***Please note, designs must be able to be screen printed on boxes***
Updates

Reason: Still debating which to choose

Target Market(s)

Designs do not have to be targeted to any specific demographic.

Industry/Entity Type

Pizza Delivery

Font styles to use
Other font styles liked:
• Please use font similar to our logo text

Requirements
Must have
• -2 or 3 ink colors
• -company name, address, phone number, URL
• -company logo and colors
• -flexibility to use on different box sizes (10x10x2, 14x14x2, 18x13x2,
• 26x18x2)
• -utilize full printable area on boxes (including 2" dimension on box sides)
• ***Please note, designs must be able to be screen printed on boxes***
Should not have
• Design features with strong similarities to existing designs of other pizzerias

```html
<!DOCTYPE html>
<html lang="en">
<head>
<meta charset="utf-8">
<title>Marco's Roostery Pizzeria – Box Design</title>
<link rel="stylesheet" href="https://fonts.googleapis.com/css2?family=Oswald:wght@500;700&display=swap">
<style>
  :root {
    --backdrop: #d8d49a;
    --brown: #6b4a3a;
    --gold: #d8a62c;
    --gold-deep: #c8962a;
    --khaki: #b6a878;
    --white: #ffffff;
  }
  html, body {
    margin: 0;
    padding: 0;
    width: 1200px;
    height: 1000px;
    overflow: hidden;
    background: var(--backdrop);
    font-family: "Oswald", sans-serif;
  }
  .canvas {
    position: relative;
    width: 1200px;
    height: 1000px;
  }
  .side-panel {
    position: absolute;
    left: 170px;
    top: 100px;
    width: 120px;
    height: 640px;
    background: var(--brown);
    border-radius: 2px;
  }
  .side-panel .stripe-fill {
    position: absolute;
    inset: 12px 14px;
    background: linear-gradient(180deg, var(--khaki), #a8996b);
  }
  .lid {
    position: absolute;
    left: 300px;
    top: 100px;
    width: 640px;
    height: 640px;
  }
  .lid svg { display: block; }
  .lid-name {
    position: absolute;
    left: 0;
    right: 0;
    top: 50%;
    transform: translateY(-50%);
    margin: 0;
    text-align: center;
    color: var(--brown);
    font-weight: 700;
    text-transform: uppercase;
    line-height: 1.1;
    white-space: nowrap;
  }
  .lid-name .line { display: block; }
  .lid-name .small { font-size: 40px; letter-spacing: 10px; }
  .lid-name .large { font-size: 88px; letter-spacing: 6px; }
  .front-panel {
    position: absolute;
    left: 300px;
    top: 752px;
    width: 640px;
    height: 130px;
    background: var(--gold);
    border-top: 10px solid var(--brown);
    border-bottom: 10px solid var(--brown);
    box-sizing: border-box;
    display: flex;
    align-items: center;
    justify-content: space-between;
    padding: 0 28px;
    color: var(--brown);
    white-space: nowrap;
  }
  .phone {
    display: flex;
    align-items: center;
    gap: 12px;
    font-size: 52px;
    font-weight: 500;
    line-height: 1;
    letter-spacing: 1px;
  }
  .phone-icon {
    width: 48px;
    height: 48px;
    flex: none;
    background: var(--brown);
    border-radius: 8px;
    display: flex;
    align-items: center;
    justify-content: center;
  }
  .brand-dot {
    width: 64px;
    height: 64px;
    flex: none;
    border: 5px solid var(--brown);
    border-radius: 50%;
    box-sizing: border-box;
  }
  .address {
    text-align: right;
    font-size: 26px;
    font-weight: 500;
    font-style: normal;
    line-height: 1.15;
    text-transform: uppercase;
  }
</style>
</head>
<body>
<main class="canvas">
  <div class="side-panel">
    <div class="stripe-fill" role="img" aria-label="Hand-drawn wavy vertical stripes in khaki on brown"></div>
  </div>

  <section class="lid">
    <svg width="640" height="640" viewBox="0 0 640 640">
      <rect x="0" y="0" width="640" height="640" fill="var(--gold-deep)" role="img" aria-label="Doodled pizza and kitchen pattern filling the corners"/>
      <rect x="40" y="40" width="560" height="560" rx="220" fill="var(--white)"/>
      <rect x="62" y="62" width="516" height="516" rx="200" fill="none" stroke="var(--gold)" stroke-width="4"/>
      <rect x="78" y="78" width="484" height="484" rx="186" fill="none" stroke="var(--gold)" stroke-width="2"/>
    </svg>
    <h1 class="lid-name">
      <span class="line small">Marco's</span>
      <span class="line large">Roostery</span>
      <span class="line small">Pizzeria</span>
    </h1>
  </section>

  <section class="front-panel">
    <div class="phone">
      <span class="phone-icon">
        <svg width="28" height="28" viewBox="0 0 24 24" aria-hidden="true">
          <path fill="var(--gold)" d="M6.6 10.8a15 15 0 0 0 6.6 6.6l2.2-2.2c.3-.3.7-.4 1-.2 1.1.4 2.3.6 3.6.6.6 0 1 .4 1 1V20c0 .6-.4 1-1 1A17 17 0 0 1 3 4c0-.6.4-1 1-1h3.5c.6 0 1 .4 1 1 0 1.3.2 2.5.6 3.6.1.3 0 .7-.2 1z"/>
        </svg>
      </span>
      <span class="phone-number">555-0148</span>
    </div>
    <span class="brand-dot" aria-hidden="true"></span>
    <address class="address">
      1472 Alder Street<br>Westbrook Plaza
    </address>
  </section>
</main>
</body>
</html>
```